Vowsbridge-Officiants.com Rack Card Design, Double-Sided. See Attachments.

Please use the attached graphics and the contents of www.vowsbridge-officiants.com to create a rack card that has the same look, feel and colors as the website, business card and existing logos. Your design must be consistent with how the business cards and website currently look.

Target Market(s)

weddings. Visit www.vowsbridge-officiants.com for content and design ideas.

Requirements
Must have
• Same info as business card plus content from the website.

```html
<!DOCTYPE html>
<html lang="en">
<head>
<meta charset="utf-8">
<title>Vowsbridge-Officiants.com Rack Card</title>
<link rel="stylesheet" href="https://fonts.googleapis.com/css2?family=Jost:wght@400;500;600&family=Bodoni+Moda:wght@400&family=Tinos:wght@400&display=swap">
<style>
  :root {
    --ink: #111111;
    --paper: #ffffff;
    --stage: #ececec;
    --gold: #c9a35a;
    --sky-top: #9fb4c4;
    --sky-mid: #c3cdd3;
    --field: #7f8a5c;
    --path: #a39782;
    --forest: #3f4a32;
    --grass: #8a9a6a;
  }
  * { box-sizing: border-box; margin: 0; padding: 0; }
  html, body { width: 1200px; height: 816px; overflow: hidden; background: var(--stage); }
  .canvas { position: relative; width: 1200px; height: 816px; }

  .rack-card {
    position: absolute; top: 84px; width: 288px; height: 648px;
    background: var(--paper); overflow: hidden;
    box-shadow: 0 6px 18px rgba(0,0,0,.18);
    font-family: "Jost", sans-serif; color: var(--ink);
  }
  .rack-card--front { left: 274px; }
  .rack-card--back { left: 638px; }

  .url-bar {
    position: absolute; left: 0; bottom: 0; width: 100%; height: 28px;
    background: var(--ink); color: var(--paper);
    font-size: 11.5px; font-weight: 500; letter-spacing: .3px;
    display: flex; align-items: center; justify-content: center;
  }

  /* Front */
  .front-photo {
    position: absolute; left: 0; top: 0; width: 100%; height: 620px;
    background:
      linear-gradient(to bottom, rgba(255,255,255,0) 0%, rgba(255,255,255,0) 72%, rgba(255,255,255,.85) 88%, var(--paper) 96%),
      linear-gradient(to bottom, var(--sky-top) 0%, var(--sky-mid) 38%, var(--field) 52%, var(--path) 75%, #b9b1a3 100%);
  }
  .brand-name {
    position: absolute; left: 0; width: 100%; text-align: center;
    font-family: "Jost", sans-serif; font-weight: 500; color: var(--ink);
  }
  .front-brand { top: 52px; font-size: 20px; letter-spacing: .2px; }
  .front-tagline {
    position: absolute; top: 124px; width: 100%; text-align: center;
    font-size: 12.5px; font-weight: 600;
  }
  .officiant-name {
    position: absolute; top: 542px; width: 100%; text-align: center;
    font-family: "Bodoni Moda", serif; font-size: 22px; letter-spacing: .4px;
  }
  .officiant-role {
    position: absolute; top: 572px; width: 100%; text-align: center;
    font-family: "Bodoni Moda", serif; font-size: 11px; letter-spacing: .5px;
  }
  .gold-rule { position: absolute; left: 50%; height: 1px; background: var(--gold); transform: translateX(-50%); }
  .front-rule { top: 588px; width: 100px; }

  /* Back */
  .back-photo {
    position: absolute; left: 0; top: 0; width: 100%; height: 130px;
    background:
      linear-gradient(to bottom, rgba(255,255,255,0) 55%, var(--paper) 100%),
      linear-gradient(to bottom, var(--forest) 0%, #55603f 45%, var(--grass) 100%);
  }
  .back-brand { top: 56px; font-size: 11.5px; color: var(--paper); display: flex; justify-content: center; align-items: center; gap: 5px; }
  .back-brand .mark { width: 7px; height: 7px; border-radius: 50%; background: var(--paper); }
  .back-intro {
    position: absolute; top: 119px; left: 40px; right: 40px; text-align: center;
    font-size: 9.6px; line-height: 12px;
  }
  .section-band {
    position: absolute; left: 20px; right: 20px; height: 22px;
    background: linear-gradient(to right, rgba(0,0,0,0) 0%, var(--ink) 30%, var(--ink) 70%, rgba(0,0,0,0) 100%);
    color: var(--paper); font-family: "Tinos", serif; font-size: 12.5px; letter-spacing: .4px;
    display: flex; align-items: center; justify-content: center;
  }
  .band-ceremonies { top: 165px; }
  .band-about { top: 322px; }
  .ceremony-list {
    position: absolute; top: 209px; left: 13px; right: 10px;
    display: grid; grid-template-columns: 1fr 1fr; column-gap: 10px;
    list-style: none; font-size: 10.2px; font-weight: 600; line-height: 12.2px;
  }
  .ceremony-list li::before { content: "• "; }
  .ceremony-list li:nth-child(n+4) { padding-left: 6px; }
  .back-note {
    position: absolute; top: 260px; left: 46px; right: 46px; text-align: center;
    font-size: 9.6px; line-height: 12px;
  }
  .about-text {
    position: absolute; top: 360px; left: 24px; right: 25px;
    font-size: 9.6px; line-height: 12px; text-align: justify; text-align-last: center;
  }
  .about-text p + p { margin-top: 12px; }
  .about-text strong { font-weight: 600; font-size: 10.2px; }
  .back-rule { top: 541px; width: 100px; }
  .contact-call {
    position: absolute; top: 566px; width: 100%; text-align: center;
    font-family: "Tinos", serif; font-size: 13.6px; line-height: 15.5px; letter-spacing: .3px;
  }
</style>
</head>
<body>
<main class="canvas">

  <section class="rack-card rack-card--front">
    <div class="front-photo" role="img" aria-label="Photograph of a barefoot bride and groom running hand in hand down a country path under a cloudy sky"></div>
    <div class="brand-name front-brand">Vowsbridge-Officiants.com</div>
    <p class="front-tagline">More Than Just a Marriage Officiant</p>
    <h1 class="officiant-name">Marisol T. Dellacroce</h1>
    <p class="officiant-role">Marriage Officiant</p>
    <div class="gold-rule front-rule"></div>
    <footer class="url-bar">www.vowsbridge-officiants.com</footer>
  </section>

  <section class="rack-card rack-card--back">
    <div class="back-photo" role="img" aria-label="Photograph of a bride and groom walking hand in hand through a tree-lined meadow"></div>
    <div class="brand-name back-brand"><span class="mark"></span>Vowsbridge-Officiants.com</div>
    <p class="back-intro">I help bring all of the pieces together on your wedding day.</p>

    <h2 class="section-band band-ceremonies">CEREMONIES</h2>
    <ul class="ceremony-list">
      <li>Unity Candles Ceremony</li>
      <li>Double Ring Ceremony</li>
      <li>Unity Sand Ceremony</li>
      <li>No Ring Ceremony</li>
      <li>Single Ring Ceremony</li>
      <li>Vow Renewals</li>
    </ul>
    <p class="back-note">I work closely with the bride and groom to customize all ceremonies or help create one unique to them.</p>

    <h2 class="section-band band-about">ABOUT ME</h2>
    <div class="about-text">
      <p><strong>I love weddings!</strong> It is my hope to inspire and share with you suggestions that help make your special day unique to you. I will be with you every step of the way providing you with all the information you need from getting your marriage license to customizing your ceremony. I have a wide network of vendors that can help us along the way and I am also a Notary Public.</p>
      <p>I truly enjoy my role as a wedding officiant. I love learning about you as a couple and seeing all the components of your wedding day come together. Your wedding day is your moment when it's just about you and your love for each other.</p>
    </div>

    <div class="gold-rule back-rule"></div>
    <p class="contact-call">CONTACT ME TO DISCUSS YOUR<br>VISION FOR YOUR SPECIAL DAY!</p>
    <footer class="url-bar">www.vowsbridge-officiants.com</footer>
  </section>

</main>
</body>
</html>
```